Online Travel Agency card design with 2 logos

Need a two sided business card design for online tourism agency which is based in Istanbul Turkey.
Need a business card design where it shows the travel agency logo but also the logo and information of the parent company as well.Parent company logo is just text with 2 different colors. (Arial font with text TemaVista "Tema"- hex #172841 and "Vista" hex-#FF7F00)
Both logos are uploaded.
Target Market(s)
travel , online
Industry/Entity Type
Travel
Contact Information for Business Card
The information on the card should be as :
Travel Agency Logo logo (RotaNova)
Parent Company logo(temalogo)
Company information :TemaVista Turizm ve Bilgi Teknolojileri A.Ş
Address of company
Tel
Email
Name
Position(english and turkish)
Look and feel
Each slider illustrates characteristics of the customer's brand and the style your logo design should communicate.

```html
<!DOCTYPE html>
<html lang="en">
<head>
<meta charset="utf-8">
<title>TemaVista Business Card</title>
<link rel="stylesheet" href="https://fonts.googleapis.com/css2?family=Open+Sans:wght@400;700&family=Marcellus&display=swap">
<style>
  :root {
    --navy: #172841;
    --orange: #FF7F00;
    --text-grey: #555555;
    --card: #ffffff;
    --backdrop: #ecebe8;
  }
  html, body {
    margin: 0;
    width: 1200px;
    height: 1200px;
    overflow: hidden;
    background: var(--backdrop);
  }
  .canvas { position: relative; width: 1200px; height: 1200px; }
  .card {
    position: absolute;
    left: 220px;
    width: 760px;
    height: 434px;
    background: var(--card);
    box-shadow: 0 6px 18px rgba(0,0,0,0.12);
    box-sizing: border-box;
  }
  .card-front { top: 110px; }
  .card-back  { top: 656px; }

  .wordmark {
    font-family: "Open Sans", Arial, sans-serif;
    font-weight: 700;
    color: var(--navy);
    letter-spacing: 0.5px;
    margin: 0;
    line-height: 1;
  }

  /* Front */
  .front-brand {
    position: absolute;
    left: 0; right: 0;
    top: 140px;
    text-align: center;
  }
  .front-brand .wordmark { font-size: 72px; }
  .company-line {
    margin: 14px 0 0;
    font-family: "Marcellus", serif;
    font-size: 21px;
    color: var(--navy);
  }
  .company-line .accent { color: var(--orange); }

  .agency-mark {
    position: absolute;
    left: 0; right: 0;
    bottom: 48px;
    display: flex;
    justify-content: center;
    align-items: center;
    gap: 10px;
    font-family: "Open Sans", Arial, sans-serif;
    font-weight: 700;
    font-size: 24px;
    color: var(--orange);
  }
  .agency-dot {
    width: 16px; height: 16px;
    border-radius: 50%;
    background: var(--orange);
  }

  /* Back */
  .back-brand {
    position: absolute;
    left: 50px;
    top: 205px;
  }
  .back-brand .wordmark { font-size: 54px; }

  .rule { position: absolute; width: 2px; background: var(--orange); }
  .rule-name { left: 400px; top: 58px; height: 74px; }
  .rule-contact { left: 430px; top: 160px; height: 86px; }
  .rule-address { left: 430px; top: 268px; height: 66px; }

  .person { position: absolute; left: 416px; top: 54px; }
  .person-name {
    margin: 0;
    font-family: "Open Sans", Arial, sans-serif;
    font-weight: 700;
    font-size: 26px;
    color: var(--orange);
    letter-spacing: 0.5px;
    line-height: 1.2;
  }
  .person-role {
    margin: 4px 0 0;
    font-family: "Marcellus", serif;
    font-size: 17px;
    color: var(--text-grey);
    line-height: 1.25;
  }

  .contact {
    position: absolute;
    left: 446px;
    top: 164px;
    margin: 0;
    padding: 0;
    list-style: none;
    font-family: "Marcellus", serif;
    font-size: 18px;
    color: var(--text-grey);
  }
  .contact li { display: flex; align-items: center; gap: 10px; height: 26px; }
  .contact svg { width: 15px; height: 15px; fill: var(--orange); flex: none; }

  .address {
    position: absolute;
    left: 446px;
    top: 272px;
    display: flex;
    gap: 10px;
    font-family: "Marcellus", serif;
    font-size: 18px;
    color: var(--text-grey);
    line-height: 1.4;
  }
  .address svg { width: 15px; height: 15px; fill: var(--orange); margin-top: 4px; flex: none; }
  .address p { margin: 0; }

  .back-agency {
    position: absolute;
    left: 50px;
    bottom: 36px;
    display: flex;
    align-items: center;
    gap: 8px;
    font-family: "Open Sans", Arial, sans-serif;
    font-weight: 700;
    font-size: 18px;
    color: var(--orange);
  }
  .back-agency .agency-dot { width: 12px; height: 12px; }
</style>
</head>
<body>
<div class="canvas">

  <section class="card card-front">
    <div class="front-brand">
      <p class="wordmark">TemaVista</p>
      <p class="company-line"><span class="accent">TemaVista Turizm</span> ve Bilgi Teknolojileri A.Ş</p>
    </div>
    <div class="agency-mark">
      <span class="agency-dot"></span>
      <span>RotaNova</span>
    </div>
  </section>

  <section class="card card-back">
    <div class="back-brand">
      <p class="wordmark">TemaVista</p>
    </div>

    <span class="rule rule-name"></span>
    <div class="person">
      <p class="person-name">SELIM ARKAN</p>
      <p class="person-role">Director<br>Direktör</p>
    </div>

    <span class="rule rule-contact"></span>
    <ul class="contact">
      <li>
        <svg viewBox="0 0 16 16"><path d="M2 6c0-2 3-4 6-4s6 2 6 4v1h-3V5.5H5V7H2zM4 8h8l2 6H2z"/></svg>
        +90-212-555-0183
      </li>
      <li>
        <svg viewBox="0 0 16 16"><circle cx="8" cy="8" r="7"/><path d="M1 8h14M8 1c3 3 3 11 0 14M8 1c-3 3-3 11 0 14" stroke="#fff" stroke-width="1" fill="none"/></svg>
        www.temavista.example
      </li>
      <li>
        <svg viewBox="0 0 16 16"><path d="M1 3h14v10H1z"/><path d="M1 3l7 6 7-6" stroke="#fff" stroke-width="1.3" fill="none"/></svg>
        selim@temavista.example
      </li>
    </ul>

    <span class="rule rule-address"></span>
    <div class="address">
      <svg viewBox="0 0 16 16"><path d="M8 1l7 7h-2v7H9.5v-4h-3v4H3V8H1z"/></svg>
      <div>
        <p>Sample city</p>
        <p>Sample country Land</p>
      </div>
    </div>

    <div class="back-agency">
      <span class="agency-dot"></span>
      <span>RotaNova</span>
    </div>
  </section>

</div>
</body>
</html>
```